Enhance the web site presence of Kolrith Global Limited

Upgrade the current web site www.kolrithpanel.com to share with the audience our current plan and future developments of our company. I have created a worksheet which shows all the pages that I like to have. The home page in English, Japanese and Chinese is hyperlinked to the various pages. Under the product, we should allow the user to select "single sided PCB or double sided PCB". The translation of the contents of the pages with Japanese is not complete but the English and Chinese are complete. You can download the briefing and photos in the dropbox files below;

https://www.sharelocker.net/sh/xk4trw92mpd3ab1/BBQm_Lp841zzPq2Rw7KtYnHjEa?dl=0

Target Market(s)

Electronic companies

Industry/Entity Type

Electronic

Coding

Coded - Design and coding required

Number of Pages Required

5+ page

Font styles to use
Sans Serif

Colors
00a990
0353a1
33b8a4

Requirements
Must have
• Get a sense of confidence on our company's integrity and capability to deliver the highest quality PCBs with the most competitive prices and best services. A sense of elegance is essential as we DON'T treat profits as the number one goal. Our number goal is to do the RIGHT things right. Having a mixture of our company photos will be appropriate.

```html
<!DOCTYPE html>
<html lang="en">
<head>
<meta charset="utf-8">
<title>Kolrith Global Limited</title>
<link href="https://fonts.googleapis.com/css2?family=Montserrat:wght@400;500;600&family=Open+Sans:wght@400;600&display=swap" rel="stylesheet">
<style>
:root{
  --green:#23855a;
  --green-dark:#1d7550;
  --green-soft:#2f9468;
  --ink:#2b2b2b;
  --muted:#6c6c6c;
  --line:#dcdcdc;
  --panel:#f1f1f1;
  --navy:#18212c;
  --navy-deep:#111820;
  --white:#ffffff;
  --accent-red:#d9192a;
}
*{box-sizing:border-box;margin:0;padding:0}
html,body{width:1200px;height:4212px;overflow:hidden}
body{position:relative;background:var(--white);font-family:"Open Sans",Arial,sans-serif;color:var(--ink)}
.abs{position:absolute}
h1,h2,h3,.heading{font-family:"Montserrat",Arial,sans-serif;font-weight:500;letter-spacing:1px}
.btn{position:absolute;background:var(--green);color:var(--white);font-family:"Montserrat",Arial,sans-serif;font-size:14px;letter-spacing:1px;display:flex;align-items:center;justify-content:center}
.body-text{font-size:15px;line-height:28px;color:var(--muted)}

/* header */
.site-header{left:0;top:0;width:1200px;height:100px;background:var(--white)}
.brand{left:84px;top:18px;font-family:"Montserrat",Arial,sans-serif;font-weight:600;font-size:34px;color:var(--ink);letter-spacing:2px}
.brand-tag{left:86px;top:60px;font-size:10px;color:var(--muted);letter-spacing:1px}
.topbar{right:250px;top:12px;display:flex;gap:34px;font-size:13px;color:var(--muted);align-items:center;white-space:nowrap}
.topbar span{display:flex;align-items:center;gap:8px}
.dot{width:20px;height:20px;border-radius:50%;background:var(--green);display:inline-block}
.nav{left:486px;top:64px;display:flex;gap:30px;font-family:"Montserrat",Arial,sans-serif;font-size:12px;color:var(--ink);letter-spacing:.5px;white-space:nowrap}
.socials{right:100px;top:13px;display:flex;gap:10px}
.socials i{width:20px;height:20px;border-radius:50%;background:var(--green);display:block}

/* hero */
.hero{left:0;top:100px;width:1200px;height:640px;background:radial-gradient(ellipse at 50% 40%,#2d3d42 0%,#18242a 55%,#0c1317 100%)}
.hero-title{left:180px;top:240px;width:840px;height:118px;border:2px solid rgba(255,255,255,.35);background:rgba(0,0,0,.35);color:var(--white);font-size:44px;font-weight:400;display:flex;align-items:center;justify-content:center;letter-spacing:2px}
.hero .btn{left:524px;top:396px;width:152px;height:50px}

/* about */
.photo{background:linear-gradient(135deg,#c9ced3,#8c96a0 60%,#5c6670)}
.about-photo{left:80px;top:800px;width:440px;height:300px}
.section-title{font-size:30px;color:var(--ink);letter-spacing:2px}
.about-title{left:592px;top:820px}
.about-rule{left:592px;top:866px;width:520px;height:1px;background:var(--line)}
.about-text{left:592px;top:888px;width:520px}

/* service cards */
.card{background:var(--panel);text-align:center}
.card .icon{position:absolute;left:50%;top:36px;transform:translateX(-50%)}
.card h3{position:absolute;left:30px;right:30px;top:118px;font-size:17px;line-height:26px;color:var(--ink)}
.card p{position:absolute;left:40px;right:40px;top:192px;font-size:13px;line-height:22px;color:var(--muted)}

/* cta band */
.cta{left:0;top:1652px;width:1200px;height:108px;background:var(--green)}
.cta-text{left:150px;top:38px;color:var(--white);font-size:21px;letter-spacing:1.5px}
.cta-btn{left:840px;top:32px;width:200px;height:46px;border:1px solid rgba(255,255,255,.7);border-radius:24px;color:var(--white);font-family:"Montserrat",Arial,sans-serif;font-size:14px;display:flex;align-items:center;justify-content:center;letter-spacing:1px}

/* investment */
.invest-title{left:88px;top:1860px}
.invest-text{left:88px;top:1930px;width:510px;font-size:14px;line-height:26px}
.invest-photo{left:680px;top:1848px;width:432px;height:286px}

/* contact */
.contact{left:0;top:2248px;width:1200px;height:512px;background:linear-gradient(160deg,var(--green-soft),var(--green-dark))}
.contact-title{left:88px;top:64px;color:var(--white);font-size:30px}
.contact-rule{left:88px;top:112px;width:532px;height:1px;background:rgba(255,255,255,.35)}
.field{border:1px solid rgba(255,255,255,.55);color:rgba(255,255,255,.75);font-size:12px;padding:10px 14px}
.submit{left:88px;top:392px;width:532px;height:42px;background:#3aa677;color:var(--white);font-family:"Montserrat",Arial,sans-serif;font-size:14px;display:flex;align-items:center;justify-content:center;letter-spacing:1px}
.avatar{left:672px;top:50px;width:88px;height:88px;border-radius:50%;background:linear-gradient(135deg,#d9b7a0,#8a5d4a);border:3px solid rgba(255,255,255,.6)}
.profile-name{left:772px;top:66px;color:var(--white);font-size:24px;letter-spacing:1.5px}
.profile-role{left:772px;top:104px;color:rgba(255,255,255,.8);font-size:11px;letter-spacing:1px}
.stars{left:880px;top:100px;display:flex;gap:4px}
.profile-text{left:772px;top:300px;width:340px;color:rgba(255,255,255,.8);font-size:13px;line-height:24px}

/* news */
.news-title{left:0;top:2856px;width:1200px;text-align:center}
.news-card{background:var(--white);box-shadow:0 0 0 1px #ececec}
.news-card h4{position:absolute;left:20px;top:32px;font-family:"Montserrat",Arial,sans-serif;font-weight:600;font-size:14px;letter-spacing:.5px;color:var(--ink)}
.news-card p{position:absolute;left:20px;top:72px;width:200px;font-size:11px;line-height:18px;color:var(--muted)}
.news-card .more{position:absolute;left:20px;top:204px;font-size:11px;color:var(--green);font-weight:600}
.news-img{position:absolute;left:236px;top:0;width:256px;height:262px;background:linear-gradient(135deg,#bcd5c6,#7aa08a 55%,#4d6e5b)}
.date{position:absolute;left:226px;top:14px;width:64px;height:72px;background:var(--green);color:var(--white);text-align:center;font-family:"Montserrat",Arial,sans-serif}
.date b{display:block;font-size:24px;font-weight:500;margin-top:8px}
.date span{font-size:14px}

/* customers */
.customers{left:0;top:3364px;width:1200px;height:416px;background:var(--panel)}
.customers-title{left:0;top:60px;width:1200px;text-align:center}
.logo-box{background:var(--white);top:164px;width:234px;height:200px;display:flex;align-items:center;justify-content:center;font-family:"Montserrat",Arial,sans-serif;font-weight:600;font-size:22px;color:#2a3f8f;letter-spacing:.5px}
.arrow{top:244px;width:28px;height:28px;border-radius:50%;background:#d8d8d8;color:var(--white);display:flex;align-items:center;justify-content:center;font-size:16px}

/* footer */
.footer{left:0;top:3780px;width:1200px;height:392px;background:var(--navy)}
.footer h5{position:absolute;font-family:"Montserrat",Arial,sans-serif;font-weight:500;font-size:15px;color:var(--white)}
.footer .line{position:absolute;display:flex;gap:14px;color:rgba(255,255,255,.7);font-size:12px;line-height:20px}
.footer .line i{flex:none;width:14px;height:14px;border-radius:50%;background:var(--green);margin-top:3px}
.news-input{left:900px;top:140px;width:200px;height:34px;border:1px solid rgba(255,255,255,.35);color:rgba(255,255,255,.6);font-size:12px;padding:8px 12px}
.news-go{left:1068px;top:140px;width:36px;height:34px;background:var(--green);color:var(--white);font-size:12px;display:flex;align-items:center;justify-content:center}
.footer-social{left:900px;top:200px;display:flex;gap:8px}
.footer-social i{width:22px;height:22px;border-radius:50%;background:rgba(255,255,255,.85);display:block}
.copyright{left:0;top:4172px;width:1200px;height:40px;background:var(--navy-deep);color:rgba(255,255,255,.55);font-size:11px;display:flex;align-items:center;justify-content:center}
</style>
</head>
<body>

<header class="site-header abs">
  <div class="brand abs">KOLRITH</div>
  <div class="brand-tag abs">GLOBAL LIMITED</div>
  <div class="topbar abs">
    <span><i class="dot"></i>info@kolrithpanel.com</span>
    <span><i class="dot"></i>+852 3906 4418</span>
  </div>
  <div class="socials abs"><i></i><i></i><i></i><i></i></div>
  <nav class="nav abs"><span>HOME</span><span>PRODUCTS</span><span>OUR FACILITIES</span><span>NEWS</span><span>CUSTOMERS</span><span>CONTACT US</span></nav>
</header>

<section class="hero abs" role="img" aria-label="Dark close-up of a printed circuit board">
  <h1 class="hero-title abs">EXCELLENCE IN QUALITY &amp; PRICE</h1>
  <div class="btn">CONTACT US</div>
</section>

<section>
  <div class="about-photo photo abs" role="img" aria-label="Business team meeting and shaking hands in an office"></div>
  <h2 class="about-title section-title abs">COMPANY BACKGROUND</h2>
  <div class="about-rule abs"></div>
  <p class="about-text body-text abs">Established in 2001, Kolrith Global Limited (KGL) is a Hong Kong company specializing in single and double sided printed circuit boards. Its manufacturing facility is located in a self owned factory in Qinglan, Guangdong of China which is 1hr travelling from Hong Kong.</p>
  <div class="btn" style="left:592px;top:1068px;width:128px;height:40px;font-size:11px">LEARN MORE</div>
</section>

<section>
  <div class="card abs" style="left:88px;top:1180px;width:492px;height:420px">
    <svg class="icon" width="64" height="64" viewBox="0 0 64 64"><circle cx="32" cy="32" r="31" fill="#fff" stroke="#ddd"/><rect x="22" y="22" width="20" height="20" fill="none" stroke="#444" stroke-width="2"/><path d="M26 22v-5M32 22v-5M38 22v-5M26 42v5M32 42v5M38 42v5M22 26h-5M22 32h-5M22 38h-5M42 26h5M42 32h5M42 38h5" stroke="#444" stroke-width="2"/></svg>
    <h3>SINGLE LAYERED PRINTED CIRCUIT BOARDS</h3>
    <p>We are offering single layered circuit boards through our own production facility in China for customers in the following industries.</p>
    <div class="btn" style="left:186px;top:300px;width:128px;height:44px;font-size:11px">LEARN MORE</div>
  </div>
  <div class="card abs" style="left:608px;top:1180px;width:504px;height:420px">
    <svg class="icon" width="64" height="64" viewBox="0 0 64 64"><circle cx="32" cy="32" r="31" fill="#fff" stroke="#ddd"/><rect x="20" y="24" width="18" height="18" fill="none" stroke="#444" stroke-width="2"/><rect x="26" y="18" width="18" height="18" fill="none" stroke="#444" stroke-width="2"/></svg>
    <h3>DOUBLE LAYERED AND MULTI-LAYERED PRINTED CIRCUIT BOARDS</h3>
    <p>We are offering double layered circuit boards through our own production facility in China for customers in the following industries.</p>
    <div class="btn" style="left:188px;top:300px;width:128px;height:44px;font-size:11px">LEARN MORE</div>
  </div>
</section>

<section class="cta abs">
  <div class="cta-text abs heading">CONTACT US TO SEE WHAT WE CAN DO FOR YOU!</div>
  <div class="cta-btn abs">CONTACT US</div>
</section>

<section>
  <h2 class="invest-title section-title abs">OUR INVESTMENT AND UPGRADE</h2>
  <p class="invest-text body-text abs">Maintaining a highly automated factory is the only way to ensure consistent product and long term competitive efficiency. From 2010 to 2017, KGL invested over US$8 million in automating our production and quality control process and enhancing our environmental processing facility.</p>
  <div class="btn" style="left:88px;top:2112px;width:128px;height:40px;font-size:11px">LEARN MORE</div>
  <div class="invest-photo photo abs" role="img" aria-label="Engineers discussing plans around a laptop"></div>
</section>

<section class="contact abs">
  <h2 class="contact-title abs">CONTACT US</h2>
  <div class="contact-rule abs"></div>
  <div class="field abs" style="left:88px;top:180px;width:256px;height:44px">Name</div>
  <div class="field abs" style="left:364px;top:180px;width:256px;height:44px">Email</div>
  <div class="field abs" style="left:88px;top:244px;width:532px;height:126px">Message</div>
  <div class="submit abs">SUBMIT</div>
  <div class="avatar abs" role="img" aria-label="Portrait of the sales contact"></div>
  <div class="profile-name abs heading">CORIN MADDOX</div>
  <div class="profile-role abs">SALES MANAGER</div>
  <div class="stars abs">
    <svg width="76" height="14" viewBox="0 0 76 14" fill="#fff"><path id="s" d="M7 0l2 5h5l-4 3 1.5 5L7 10l-4.5 3L4 8 0 5h5z"/><use href="#s" x="15"/><use href="#s" x="30"/><use href="#s" x="45"/><use href="#s" x="60" opacity=".4"/></svg>
  </div>
  <p class="profile-text abs">Here to answer your questions about quotations, lead times and technical specifications. Send us a message and we will reply within one business day.</p>
</section>

<section>
  <h2 class="news-title section-title abs">OUR RECENT NEWS</h2>
  <article class="news-card abs" style="left:88px;top:2984px;width:492px;height:262px">
    <h4>LOREM IPSUM DOLOR</h4>
    <p>It is a long established fact that a reader will be distracted by the readable content of a page when looking at its layout.</p>
    <span class="more">Read More..</span>
    <div class="news-img" role="img" aria-label="Factory floor with circuit board production machines"></div>
    <div class="date"><b>29</b><span>Nov</span></div>
  </article>
  <article class="news-card abs" style="left:620px;top:2984px;width:492px;height:262px">
    <h4>LOREM IPSUM DOLOR</h4>
    <p>It is a long established fact that a reader will be distracted by the readable content of a page when looking at its layout.</p>
    <span class="more">Read More..</span>
    <div class="news-img" role="img" aria-label="Automated circuit board assembly line" style="background:linear-gradient(135deg,#d6c8b4,#9a8772 55%,#5e4e40)"></div>
    <div class="date"><b>29</b><span>Nov</span></div>
  </article>
</section>

<section class="customers abs">
  <h2 class="customers-title section-title abs">OUR CUSTOMERS</h2>
  <div class="arrow abs" style="left:20px">&#8249;</div>
  <div class="logo-box abs" style="left:80px">Norvale Trade</div>
  <div class="logo-box abs" style="left:348px">Petronel</div>
  <div class="logo-box abs" style="left:612px;color:#555">Halvex Circuits</div>
  <div class="logo-box abs" style="left:880px;color:var(--accent-red)">Zentoku</div>
  <div class="arrow abs" style="left:1152px">&#8250;</div>
</section>

<footer class="footer abs">
  <h5 style="left:88px;top:60px">Contact Information</h5>
  <div class="line" style="left:88px;top:110px;width:300px"><i></i><span>Kolrith Global Limited, Unit 1208, Harbourline Tower, 88 Marlow Road, Hong Kong</span></div>
  <div class="line" style="left:88px;top:220px"><i></i><span>+852 3906 4418</span></div>
  <div class="line" style="left:88px;top:286px"><i></i><span>sales@kolrithpanel.com</span></div>
  <h5 style="left:480px;top:60px">Contact Information</h5>
  <div class="line" style="left:480px;top:110px;width:320px"><i></i><span>Kolrith Global (Qinglan) Limited, No. 6 Fenwick Industrial Road, Qinglan Town, Guangdong, China</span></div>
  <div class="line" style="left:480px;top:220px"><i></i><span>+86 769 2210 5573</span></div>
  <div class="line" style="left:480px;top:286px"><i></i><span>sales@kolrithpanel.com</span></div>
  <h5 style="left:900px;top:60px">Newsletter</h5>
  <div class="news-input abs">Your Email</div>
  <div class="news-go abs">Go</div>
  <div class="footer-social abs"><i></i><i></i><i></i><i></i><i></i></div>
</footer>
<div class="copyright abs">Copyright &copy; 2017 Kolrith Global Limited. All Rights Reserved.</div>

</body>
</html>
```